Need a stunning looking Business Card Design for my Telecom Business, Wow FACTOR!

I deal with high level IT Directors , and Contractors.
I need to impress them with a sleek , professional and unique business card.
Im thinking options as far as rounded edges, plastic , or even metal card or die cut on a corner.
Whatever looks better and leave an unforgettable first impression.
im looking for the wow factor.
Front should have the basics info (attached on the picture of current business card)
i would like to add picture of myself somewhere
Back side
should have logo and maybe some pictures or past projects, you can download from my website ( www.lumvexholdings.com)

```html
<!DOCTYPE html>
<html lang="en">
<head>
<meta charset="utf-8">
<title>Lumvex Technologies – Business Card</title>
<link href="https://fonts.googleapis.com/css2?family=Montserrat:wght@400;500;700&display=swap" rel="stylesheet">
<style>
  :root{
    --backdrop:#a8a8a8;
    --card-white:#ffffff;
    --brand-blue:#0b5688;
    --ink:#1c1c1c;
    --faint:#f2f4f7;
    --on-blue:#ffffff;
  }
  html,body{margin:0;padding:0;overflow:hidden;}
  body{width:900px;height:1200px;background:var(--backdrop);font-family:'Montserrat',sans-serif;position:relative;}
  .card{position:absolute;left:80px;width:742px;height:438px;border-radius:36px;overflow:hidden;}
  .card-front{top:130px;background:var(--card-white);}
  .card-back{top:638px;background:var(--brand-blue);}

  .front-brand{position:absolute;left:40px;top:38px;display:flex;align-items:center;gap:16px;}
  .brand-dot{width:46px;height:46px;border-radius:50%;background:var(--brand-blue);}
  .brand-name{color:var(--ink);font-weight:500;font-size:30px;letter-spacing:2px;line-height:1;}
  .brand-name .sub{display:block;font-size:14px;letter-spacing:7px;margin-top:6px;text-align:center;}

  .faint-circle{position:absolute;right:-20px;top:30px;width:250px;height:250px;border-radius:50%;background:var(--faint);}

  .person{position:absolute;left:50px;top:244px;}
  .person-name{margin:0;color:var(--brand-blue);font-size:26px;font-weight:400;letter-spacing:.5px;line-height:1;}
  .person-name strong{font-weight:700;}
  .person-role{margin:6px 0 0;font-size:15px;color:var(--ink);}

  .divider{position:absolute;left:50px;top:300px;width:656px;height:2px;background:var(--brand-blue);}
  .license{position:absolute;left:444px;top:301px;width:262px;height:30px;background:var(--brand-blue);color:var(--on-blue);font-size:15px;line-height:30px;padding-left:33px;box-sizing:border-box;clip-path:polygon(12px 0,100% 0,100% 100%,0 100%);}

  .contacts{position:absolute;left:52px;top:332px;margin:0;padding:0;list-style:none;font-size:16px;color:var(--ink);}
  .contacts li{display:flex;align-items:center;gap:10px;height:23.5px;}
  .contacts svg{width:14px;height:14px;fill:var(--brand-blue);}

  .offices{position:absolute;left:441px;top:344px;font-size:16px;color:var(--ink);line-height:21px;}
  .offices-title{margin:0 0 1px;color:var(--brand-blue);font-weight:700;font-size:18px;}
  .offices p{margin:0;}

  .back-brand{position:absolute;left:0;right:0;top:70px;display:flex;flex-direction:column;align-items:center;color:var(--on-blue);}
  .back-dot{width:150px;height:150px;border-radius:50%;background:var(--on-blue);opacity:.95;margin-bottom:58px;}
  .back-name{font-weight:500;font-size:48px;letter-spacing:5px;line-height:1;text-align:center;}
  .back-name .sub{display:block;font-size:18px;letter-spacing:11px;margin-top:12px;}
</style>
</head>
<body>
  <section class="card card-front" aria-label="Card front">
    <div class="faint-circle"></div>
    <div class="front-brand">
      <span class="brand-dot"></span>
      <span class="brand-name">LUMVEX<span class="sub">TECHNOLOGIES</span></span>
    </div>

    <div class="person">
      <h1 class="person-name"><strong>REID</strong> CALLOWAY</h1>
      <p class="person-role">Operation Manager</p>
    </div>

    <div class="divider"></div>
    <div class="license">State License #EX40028813</div>

    <ul class="contacts">
      <li><svg viewBox="0 0 24 24"><path d="M6.6 10.8a15.1 15.1 0 0 0 6.6 6.6l2.2-2.2a1 1 0 0 1 1-.25 11.4 11.4 0 0 0 3.6.57 1 1 0 0 1 1 1V20a1 1 0 0 1-1 1A17 17 0 0 1 3 4a1 1 0 0 1 1-1h3.5a1 1 0 0 1 1 1c0 1.250.2 2.450.57 3.570a1 1 0 0 1-.25 1z"/></svg>(555) 318-4702</li>
      <li><svg viewBox="0 0 24 24"><path d="M2 5h20v2l-10 6L2 7zm0 4 10 6 10-6v10H2z"/></svg>www.lumvexholdings.com</li>
      <li><svg viewBox="0 0 24 24"><circle cx="12" cy="12" r="10"/></svg>info@lumvexholdings.com</li>
    </ul>

    <div class="offices">
      <p class="offices-title">Lumvex Technologies</p>
      <p>Offices in Harborview, Eastvale</p>
      <p>&amp; Cedar Point</p>
    </div>
  </section>

  <section class="card card-back" aria-label="Card back">
    <div class="back-brand">
      <span class="back-dot"></span>
      <span class="back-name">LUMVEX<span class="sub">TECHNOLOGIES</span></span>
    </div>
  </section>
</body>
</html>
```